Tidewell Recovery Business Card Design

Professional and clean design. The design colors should flow with the logo. Two-sided card with the website on the back which is:

www.TidewellRecovery.example.

"Specializing in Water Damage Restoration"

On the front I need the name, email, phone, and logo.

Name: Dorian Vashti
Email: Dorian@TidewellRecovery.example
Phone: 555-318-2046 for now

I only have the Preview and Thumbnail right now but should have the source files uploaded within a day or two.

Target Market(s)

Flood victims, home owners with water damage from busted pipes etc...

Industry/Entity Type

Business

Contact Information for Business Card

Name: Dorian Vashti

Font styles to use
Serif
Sans Serif

```html
<!DOCTYPE html>
<html lang="en">
<head>
<meta charset="utf-8">
<title>Tidewell Recovery Business Cards</title>
<link rel="stylesheet" href="https://fonts.googleapis.com/css2?family=Cinzel:wght@500&family=Fjalla+One&display=swap">
<style>
  :root {
    --page: #1b1d20;
    --card-blue: #5d9dc5;
    --card-blue-deep: #4f8fb8;
    --water-light: #dcebf3;
    --water-mid: #a9cde0;
    --silver: #dfe4e8;
    --ink-slate: #3a4650;
    --white: #ffffff;
  }
  * { box-sizing: border-box; margin: 0; padding: 0; }
  html, body { width: 1200px; height: 1200px; overflow: hidden; background: var(--page); }
  .canvas { position: relative; width: 1200px; height: 1200px; }

  .card {
    position: absolute;
    left: 180px;
    width: 840px;
    height: 470px;
    background: linear-gradient(180deg, var(--card-blue) 0%, var(--card-blue-deep) 100%);
    overflow: hidden;
    text-align: center;
  }
  .card--brand { top: 90px; }
  .card--contact { top: 640px; }

  .notch {
    position: absolute;
    width: 76px;
    height: 76px;
    border-radius: 50%;
    background: var(--page);
    z-index: 3;
  }
  .notch--left { left: -38px; top: 250px; }
  .notch--right { right: -38px; top: 160px; }
  .card--contact .notch--left { top: 210px; }
  .card--contact .notch--right { top: 280px; }

  .water {
    position: absolute;
    left: 0; right: 0; bottom: 0;
    height: 44%;
    background: linear-gradient(180deg, rgba(169,205,224,0) 0%, var(--water-mid) 40%, var(--water-light) 75%, var(--water-mid) 100%);
    z-index: 1;
  }
  .card--contact .water { height: 48%; }

  .content { position: relative; z-index: 2; }

  .mark {
    display: block;
    margin: 0 auto;
    border-radius: 50%;
    background: var(--silver);
  }
  .card--brand .mark { width: 150px; height: 150px; margin-top: 52px; }
  .card--contact .mark { width: 84px; height: 84px; margin-top: 40px; }

  .brand-name {
    font-family: "Cinzel", serif;
    font-weight: 500;
    color: var(--silver);
    line-height: 1.05;
    letter-spacing: 0.04em;
  }
  .card--brand .brand-name { font-size: 68px; margin-top: 28px; }
  .card--contact .brand-name { font-size: 40px; margin-top: 18px; }

  .tagline {
    font-family: "Fjalla One", sans-serif;
    color: var(--ink-slate);
    font-size: 27px;
    letter-spacing: 0.02em;
    margin-top: 62px;
  }

  .person {
    font-family: "Fjalla One", sans-serif;
    color: var(--white);
    font-size: 60px;
    line-height: 1;
    margin-top: 62px;
  }
  .email, .website {
    font-family: "Fjalla One", sans-serif;
    color: var(--ink-slate);
    font-size: 21px;
  }
  .email { margin-top: 14px; }
  .phone {
    font-family: "Fjalla One", sans-serif;
    color: var(--ink-slate);
    font-size: 36px;
    line-height: 1.1;
  }
</style>
</head>
<body>
<main class="canvas">
  <section class="card card--brand">
    <div class="water" role="img" aria-label="Rippling water surface along the bottom of the card"></div>
    <span class="notch notch--left"></span>
    <span class="notch notch--right"></span>
    <div class="content">
      <span class="mark"></span>
      <h1 class="brand-name">Tidewell Recovery</h1>
      <p class="tagline">SPECIALIZING IN WATER DAMAGE RESTORATION</p>
    </div>
  </section>

  <section class="card card--contact">
    <div class="water" role="img" aria-label="Rippling water surface along the bottom of the card"></div>
    <span class="notch notch--left"></span>
    <span class="notch notch--right"></span>
    <div class="content">
      <span class="mark"></span>
      <p class="brand-name">Tidewell Recovery</p>
      <h2 class="person">DORIAN Vashti</h2>
      <p class="email">Dorian@TidewellRecovery.example</p>
      <p class="phone">555-318-2046</p>
      <p class="website">www.TidewellRecovery.example</p>
    </div>
  </section>
</main>
</body>
</html>
```